Logo and Card design for KLV Home Solutions LLC

I need an edgier logo and business card designs. Current logo attached. I like the colors below. I would like the logo to incorporate a home in the design.
Title = Principal-Acquisitions
Email:KLVHOMESOLUTIONS@maplenest-mail.com
412-907-2153
facebook
IG
2 sided business card with the front being contact info a slogan about selling a home fast. The back incorporating What we do. Buy houses, land, or commercial property as is. We find solutions to make the process of selling simple and fair.

Target Market(s)

Motivated house sellers.

Industry/Entity Type

Business

Contact Information for Business Card

Who we are: We are a Faith based Real Estate Investment Company. We pay cash for homes in any condition and can close quick. Whatever the reason you need to sell fast, we can help. We believe in creating win-win solutions to help you in your time of need. We care! We can help!

Logo Text

KLV Home Solutions LLC

Font styles to use
Sans Serif

Colors
33a6d7
0355a3
85abd2
cee9f5
9d9d9d
b2b2b2
ffffff

Requirements
Must have
• Old logo attached. I want something edgier.
• Company name, phone number, description on the back of what we can do. Pay all cash. Buy in as is condition. No fees,Commisions or closing costs.Close quick. No hassles with solutions to meet your unique situation.
• Call today for an offer within 24 hours.

```html
<!DOCTYPE html>
<html lang="en">
<head>
<meta charset="utf-8">
<title>KLV Home Solutions – Business Card</title>
<link href="https://fonts.googleapis.com/css2?family=Montserrat:wght@500;600;700&family=Roboto:wght@400;500&display=swap" rel="stylesheet">
<style>
  :root {
    --sky: #33a6d7;
    --navy: #0355a3;
    --mist: #85abd2;
    --ice: #cee9f5;
    --stone: #9d9d9d;
    --silver: #b2b2b2;
    --white: #ffffff;
    --backdrop: #cbcbcb;
    --ink: #111111;
  }
  * { margin: 0; padding: 0; box-sizing: border-box; }
  html, body { width: 900px; height: 1200px; overflow: hidden; }
  body {
    position: relative;
    background: radial-gradient(ellipse at 50% 45%, #dedede 0%, var(--backdrop) 75%);
    font-family: "Roboto", Arial, sans-serif;
  }
  .card {
    position: absolute;
    left: 82px;
    width: 733px;
    height: 430px;
    border-radius: 24px;
    overflow: hidden;
    background: linear-gradient(180deg, #ffffff 0%, #f2f2f2 60%, #e9e9e9 100%);
    box-shadow: 0 4px 10px rgba(0,0,0,0.35);
  }
  .card--front { top: 137px; }
  .card--back { top: 633px; }

  .brand {
    position: absolute;
    left: 0; right: 0;
    display: flex;
    justify-content: center;
    align-items: center;
    gap: 14px;
    font-family: "Montserrat", Arial, sans-serif;
    font-weight: 700;
    font-size: 42px;
    letter-spacing: 0.5px;
    color: var(--navy);
  }
  .brand__square { width: 26px; height: 26px; background: var(--navy); }
  .card--front .brand { top: 168px; }
  .card--back .brand { top: 166px; }

  .divider {
    position: absolute; left: 0; right: 0; top: 291px;
    height: 7px; background: var(--silver);
  }
  .contact-band {
    position: absolute; left: 0; right: 0; top: 303px; height: 115px;
    background: linear-gradient(90deg, var(--navy) 0%, #1a78bd 55%, var(--sky) 100%);
    color: var(--white);
  }
  .person { position: absolute; left: 45px; top: 20px; }
  .person__name {
    font-family: "Montserrat", Arial, sans-serif;
    font-weight: 700; font-size: 24px;
  }
  .person__title { font-size: 16px; margin-top: 4px; }
  .contact-list { position: absolute; left: 384px; top: 18px; list-style: none; }
  .contact-list li {
    display: flex; align-items: center; gap: 10px;
    font-size: 16px; height: 29px;
  }
  .contact-list svg { width: 17px; height: 17px; fill: var(--white); }

  .social-tab {
    position: absolute; right: 0; bottom: 0; width: 270px; height: 34px;
  }
  .social-tab__shape { position: absolute; inset: 0; }
  .social-tab__content {
    position: absolute; left: 36px; top: 5px;
    display: flex; align-items: center; gap: 10px;
    font-size: 16px; color: #333;
  }
  .social-tab__dot { width: 14px; height: 14px; border-radius: 50%; background: var(--navy); }

  .services {
    position: absolute; left: 0; right: 0; top: 322px;
    text-align: center; font-size: 16px; line-height: 24px; color: var(--ink);
  }
  .cta {
    position: absolute; left: 35px; width: 663px; top: 386px; height: 26px;
    border-radius: 13px;
    background: linear-gradient(90deg, #2d5fae 0%, #4a7cc0 45%, var(--mist) 75%, #3d69b4 100%);
    color: var(--white); font-size: 16px; font-weight: 500;
    display: flex; align-items: center; justify-content: center;
  }
</style>
</head>
<body>

<section class="card card--front" aria-label="Business card front">
  <div class="brand"><span class="brand__square"></span>KLV HOME SOLUTIONS</div>
  <div class="divider"></div>
  <div class="contact-band">
    <div class="person">
      <div class="person__name">Marcus Reed</div>
      <div class="person__title">Principal-Acquisitions</div>
    </div>
    <ul class="contact-list">
      <li>
        <svg viewBox="0 0 24 24" aria-hidden="true"><path d="M6.6 10.8a15.1 15.1 0 0 0 6.6 6.6l2.2-2.2c.3-.3.7-.4 1-.2 1.1.4 2.3.6 3.6.6.6 0 1 .4 1 1V20c0 .6-.4 1-1 1A17 17 0 0 1 3 4c0-.6.4-1 1-1h3.5c.6 0 1 .4 1 1 0 1.3.2 2.5.6 3.6.1.3 0 .7-.2 1z"/></svg>
        412-907-2153
      </li>
      <li>
        <svg viewBox="0 0 24 24" aria-hidden="true"><path d="M2 5h20v14H2zm2 2v.5l8 5 8-5V7zm0 2.8V17h16V9.8l-8 5z"/></svg>
        KLVHOMESOLUTIONS@maplenest-mail.com
      </li>
    </ul>
  </div>
  <div class="social-tab">
    <svg class="social-tab__shape" viewBox="0 0 270 34" preserveAspectRatio="none" aria-hidden="true">
      <path d="M0 34 C12 34 14 0 32 0 H270 V34 Z" fill="#f0f0f0"/>
    </svg>
    <div class="social-tab__content"><span class="social-tab__dot"></span>Klvhomesolutions</div>
  </div>
</section>

<section class="card card--back" aria-label="Business card back">
  <div class="brand"><span class="brand__square"></span>KLV HOME SOLUTIONS</div>
  <p class="services">Pay all cash. Buy in as is condition. No fees,Commisions or closing costs.Close quick.<br>No hassles with solutions to meet your unique situation.</p>
  <div class="cta">Call today for an offer within 24 hours.</div>
</section>

</body>
</html>
```